Ferncrest Dental, LLC business card project

Business card to be designed with current logo.
Dental office- please keep design of card that looks clean and professional.
Please include the following info:
Ferncrest Dental, LLC
Dr. Lorna Pettigrew
2871 Marlowe Street
Bethlehem, PA 18093
610-555-0193
ferncrestdental.office@examplemail.test
Hello everyone-
Reason: Just got back from overseas- will look at all designs and provide feedback. Thank you!
Reason: Polling my friends for the final selection-
thank you to all those that participated- so many talented designers!

```html
<!DOCTYPE html>
<html lang="en">
<head>
<meta charset="utf-8">
<title>Ferncrest Dental, LLC — Business Card</title>
<link rel="stylesheet" href="https://fonts.googleapis.com/css2?family=Questrial&family=Arimo:ital,wght@1,700&display=swap">
<style>
  :root {
    --page: #ffffff;
    --card-grey: #6b6c70;
    --panel-light: #8f9094;
    --lime: #a9c93b;
    --lime-text: #b4cd3c;
    --shadow: rgba(0, 0, 0, 0.28);
  }
  * { box-sizing: border-box; margin: 0; padding: 0; }
  html, body {
    width: 1088px; height: 1200px; overflow: hidden;
    background: var(--page);
  }
  .canvas { position: relative; width: 1088px; height: 1200px; }

  .card {
    position: absolute;
    background: var(--card-grey);
    border-radius: 23px;
    overflow: hidden;
    box-shadow: 0 2px 6px var(--shadow);
  }

  /* Front */
  .card--front { left: 60px; top: 13px; width: 882px; height: 502px; }
  .front__panel {
    position: absolute; left: 366px; top: 0; right: 0; height: 392px;
    background: radial-gradient(ellipse 70% 90% at 75% 5%, var(--panel-light), var(--card-grey) 85%);
  }
  .front__divider {
    position: absolute; left: 363px; top: 0; width: 3px; height: 100%;
    background: var(--lime);
  }
  .front__band {
    position: absolute; left: 366px; right: 0; top: 392px; height: 21px;
    background: var(--lime);
  }

  .brand { position: absolute; display: flex; align-items: center; white-space: nowrap; }
  .brand__dot { border-radius: 50%; background: var(--lime); flex: none; }
  .brand__name {
    font-family: "Questrial", "Century Gothic", sans-serif;
    color: var(--lime); font-weight: 400; letter-spacing: -0.5px;
  }
  .card--front .brand { left: 17px; top: 102px; gap: 8px; }
  .card--front .brand__dot { width: 20px; height: 20px; }
  .card--front .brand__name { font-size: 28px; }

  .person {
    position: absolute; left: 388px; top: 192px;
    font-family: Arial, "Arimo", sans-serif;
    font-size: 23px; color: var(--lime-text);
    padding-bottom: 1px;
    border-bottom: 1px solid var(--lime-text);
  }
  .contact {
    position: absolute; left: 389px; top: 252px;
    list-style: none;
    font-family: "Arimo", Arial, sans-serif;
    font-style: italic; font-weight: 700;
    font-size: 16.5px; color: var(--lime-text);
  }
  .contact__item { display: flex; align-items: flex-start; gap: 13px; margin-bottom: 17px; }
  .contact__icon { width: 27px; height: 24px; flex: none; }
  .contact__text { line-height: 22px; }

  /* Back */
  .card--back { left: 55px; top: 546px; width: 884px; height: 504px; }
  .card--back .brand { left: 0; right: 0; top: 140px; justify-content: center; gap: 16px; }
  .card--back .brand__dot { width: 44px; height: 44px; }
  .card--back .brand__name { font-size: 58px; letter-spacing: -1px; }
  .back__swoosh { position: absolute; left: 0; top: 0; width: 884px; height: 504px; }
</style>
</head>
<body>
<main class="canvas">

  <section class="card card--front" aria-label="Card front">
    <div class="front__panel"></div>
    <div class="front__divider"></div>
    <div class="front__band"></div>

    <div class="brand">
      <span class="brand__dot"></span>
      <span class="brand__name">Ferncrest Dental, LLC</span>
    </div>

    <p class="person">Dr. Lorna Pettigrew</p>

    <ul class="contact">
      <li class="contact__item">
        <svg class="contact__icon" viewBox="0 0 27 24" fill="none" stroke="#b4cd3c" stroke-width="2">
          <rect x="3" y="2" width="21" height="20" rx="3"/>
          <path d="M9 7c-1 3 2 8 6 10l2-2-2-2-1.5 1c-1.5-1-3-3-3.5-4.5L11 8 9 6z" fill="#b4cd3c" stroke="none"/>
        </svg>
        <span class="contact__text">610-555-0193</span>
      </li>
      <li class="contact__item">
        <svg class="contact__icon" viewBox="0 0 27 24" fill="none" stroke="#b4cd3c" stroke-width="2">
          <path d="M3 10 13.5 3 24 10v12H3z"/>
          <path d="M3 10l10.5 7L24 10M3 22l8-6M24 22l-8-6"/>
        </svg>
        <span class="contact__text">ferncrestdental.office@examplemail.test</span>
      </li>
      <li class="contact__item">
        <svg class="contact__icon" viewBox="0 0 27 24" fill="none" stroke="#b4cd3c" stroke-width="2">
          <path d="M2 12 13.5 2 25 12"/>
          <path d="M5 10v13h17V10"/>
          <path d="M11 23v-7h5v7"/>
        </svg>
        <span class="contact__text">2871 Marlowe Street<br>Bethlehem, PA 18093</span>
      </li>
    </ul>
  </section>

  <section class="card card--back" aria-label="Card back">
    <svg class="back__swoosh" viewBox="0 0 884 504" aria-hidden="true">
      <path d="M104 504C300 385 540 330 700 335C790 338 850 350 884 360V504Z" fill="#a9c93b"/>
    </svg>
    <div class="brand">
      <span class="brand__dot"></span>
      <span class="brand__name">Ferncrest Dental, LLC</span>
    </div>
  </section>

</main>
</body>
</html>
```